Email Banner: Brightfold

Need an email banner for https://brightfold-hub.io/ much the same design for the attatched just using the logo and brand as the guidance.

Tagline should be "Essential Whitepapers for Business Professionals" or "Whitepapers featured from the most reputable companies in the industry"

It will be going on an email that looks like this:

https://mailvista-demo.co/emails/preview/fullscreen/a71b3d2e-9c4f-4e8a-b12d-f05e6a8c1b3d

So dont make it to thick and clunky.

Target Market(s)

IT Proffesioanls

Industry/Entity Type

Information Technology

Logo Text

Essential Whitepapers for Business Professionals

Logo styles of interest
Abstract Logo
Font styles to use
Sans Serif

Colors
0054AA
0677BA
7BADD7
CADEEF
E8F1F8

Requirements
Must have
• Logo and colour scheme from the weblink provided: https://brightfold-hub.io/

```html
<!DOCTYPE html>
<html lang="en">
<head>
<meta charset="utf-8">
<title>Brightfold Email Banner</title>
<link rel="stylesheet" href="https://fonts.googleapis.com/css2?family=Red+Hat+Display:wght@500;700;800&display=swap">
<style>
  :root {
    --stage: #01022a;
    --panel-white: #ffffff;
    --violet: #3f00c0;
    --cta: #2a06e6;
    --stripe-start: #2d12e0;
    --stripe-end: #0a8cf5;
    --ink: #0d0b2e;
    --mark-start: #5a10e0;
    --mark-end: #1a7cf0;
    --text-light: #ffffff;
  }
  * { box-sizing: border-box; margin: 0; padding: 0; }
  html, body {
    width: 1200px; height: 1200px; overflow: hidden;
    background: var(--stage);
    font-family: "Red Hat Display", Arial, sans-serif;
  }
  .canvas { position: relative; width: 1200px; height: 1200px; }
  .banner {
    position: absolute; left: 118px; width: 964px; height: 151px;
    background: var(--violet); overflow: hidden;
  }
  .banner--wide { top: 387px; }
  .banner--stacked { top: 661px; }
  .banner__shapes { position: absolute; inset: 0; width: 964px; height: 151px; }
  .brand {
    position: absolute; top: 0; height: 151px; left: 22px;
    display: flex; align-items: center; gap: 12px;
    color: var(--ink); font-weight: 700; letter-spacing: -0.01em;
  }
  .brand__dot {
    border-radius: 50%;
    background: linear-gradient(135deg, var(--mark-start), var(--mark-end));
  }
  .banner--wide .brand__dot { width: 30px; height: 30px; }
  .banner--wide .brand__name { font-size: 34px; }
  .banner--stacked .brand__dot { width: 44px; height: 44px; }
  .banner--stacked .brand__name { font-size: 40px; }
  .tagline {
    position: absolute; left: 377px; top: 37px;
    color: var(--text-light); font-size: 27px; font-weight: 500; line-height: 36px;
  }
  .tagline strong { font-weight: 700; }
  .cta {
    position: absolute; right: 0; top: 0; width: 169px; height: 44px;
    display: flex; align-items: center; justify-content: flex-end; padding-right: 20px;
    color: var(--text-light); font-size: 18px; font-weight: 800; letter-spacing: 0.01em;
  }
</style>
</head>
<body>
<main class="canvas">

  <section class="banner banner--wide" aria-label="Brightfold banner, inline wordmark">
    <svg class="banner__shapes" viewBox="0 0 964 151" aria-hidden="true">
      <defs>
        <linearGradient id="stripe-a" x1="0" y1="0" x2="0" y2="1">
          <stop offset="0" stop-color="var(--stripe-start)"/>
          <stop offset="1" stop-color="var(--stripe-end)"/>
        </linearGradient>
      </defs>
      <polygon points="263,0 299,0 377,151 349,151" fill="url(#stripe-a)"/>
      <polygon points="0,0 263,0 349,151 0,151" fill="var(--panel-white)"/>
      <polygon points="795,0 964,0 964,44 822,44" fill="var(--cta)"/>
    </svg>
    <div class="brand"><span class="brand__dot"></span><span class="brand__name">Brightfold</span></div>
    <p class="tagline">Essential Whitepapers<br>for <strong>Business Professionals</strong></p>
    <a class="cta">CLICK HERE</a>
  </section>

  <section class="banner banner--stacked" aria-label="Brightfold banner, large wordmark">
    <svg class="banner__shapes" viewBox="0 0 964 151" aria-hidden="true">
      <defs>
        <linearGradient id="stripe-b" x1="0" y1="0" x2="0" y2="1">
          <stop offset="0" stop-color="var(--stripe-start)"/>
          <stop offset="1" stop-color="var(--stripe-end)"/>
        </linearGradient>
      </defs>
      <polygon points="263,0 299,0 377,151 349,151" fill="url(#stripe-b)"/>
      <polygon points="0,0 263,0 349,151 0,151" fill="var(--panel-white)"/>
      <polygon points="795,0 964,0 964,44 822,44" fill="var(--cta)"/>
    </svg>
    <div class="brand"><span class="brand__dot"></span><span class="brand__name">Brightfold</span></div>
    <p class="tagline">Essential Whitepapers<br>for <strong>Business Professionals</strong></p>
    <a class="cta">CLICK HERE</a>
  </section>

</main>
</body>
</html>
```